In need a simple business/calling card

I am looking for a VERY simple, professional, and classic business card which is really more of a calling card. In the Halvorsen & Pike or Whitlow kind of style. I am also open to a solid boarder but not necessary. I prefer no logos or "designs".

Target Market(s)

general

Contact Information for Business Card

Daniel Brenwick (or Daniel T. Brenwick)
+1 555 274 6180
dan@brenwick.example

Thats it!

Font styles to use
Serif
Sans Serif
Script

Colors

Designer to choose colors to be used in the design.

Requirements
Must have
• everything on the card details section.
Nice to have
• n/a
Should not have
• No logos.

```html
<!DOCTYPE html>
<html lang="en">
<head>
<meta charset="utf-8">
<title>Daniel Brenwick — Calling Card</title>
<link rel="stylesheet" href="https://fonts.googleapis.com/css2?family=Barlow:wght@300;600&family=Nunito+Sans:wght@400&display=swap">
<style>
  :root {
    --backdrop: #ecebea;
    --card: #1d2136;
    --card-glow: #22273e;
    --ink: #d9d5d5;
    --shadow: rgba(0, 0, 0, 0.28);
  }
  * { margin: 0; padding: 0; box-sizing: border-box; }
  html, body {
    width: 1200px;
    height: 1000px;
    overflow: hidden;
    background: var(--backdrop);
  }
  .card {
    position: absolute;
    left: 207px;
    top: 276px;
    width: 788px;
    height: 449px;
    background: var(--card);
    box-shadow: 3px 4px 8px var(--shadow);
    color: var(--ink);
  }
  .card__ornament-area {
    position: absolute;
    left: 193px;
    top: 100px;
    width: 400px;
    height: 200px;
    background: radial-gradient(ellipse at center, var(--card-glow) 0%, var(--card) 70%);
  }
  .card__name {
    position: absolute;
    left: 0;
    right: 0;
    top: 155px;
    text-align: center;
    font-family: "Barlow", sans-serif;
    font-size: 68px;
    line-height: 80px;
    letter-spacing: 0.5px;
    white-space: nowrap;
  }
  .card__name-first { font-weight: 300; }
  .card__name-last { font-weight: 600; margin-left: 10px; }
  .card__contact {
    position: absolute;
    top: 384px;
    display: flex;
    align-items: center;
    gap: 8px;
    font-family: "Nunito Sans", sans-serif;
    font-size: 26px;
    letter-spacing: 1.2px;
    white-space: nowrap;
  }
  .card__contact--phone { left: 45px; }
  .card__contact--email { right: 38px; }
  .card__icon { width: 28px; height: 24px; flex: none; }
  .card__icon path { fill: var(--ink); }
</style>
</head>
<body>
  <div class="card">
    <div class="card__ornament-area" role="img" aria-label="Area reserved for a subtle decorative accent around the name"></div>

    <h1 class="card__name">
      <span class="card__name-first">Daniel</span><span class="card__name-last">Brenwick</span>
    </h1>

    <p class="card__contact card__contact--phone">
      <svg class="card__icon" viewBox="0 0 28 24" aria-hidden="true">
        <path d="M2 8 Q14 0 26 8 L26 11 L20 11 L19 8 Q14 6 9 8 L8 11 L2 11 Z"/>
        <path d="M7 12 L21 12 L25 22 L3 22 Z M14 14.5 A3 3 0 1 0 14 20.5 A3 3 0 1 0 14 14.5 Z"/>
      </svg>
      <span>+1 555 274 6180</span>
    </p>

    <p class="card__contact card__contact--email">
      <svg class="card__icon" viewBox="0 0 28 24" aria-hidden="true">
        <path d="M1 4 H27 V20 H1 Z M3.5 6 L14 14 L24.5 6 Z M3 8 V18 L10 13 Z M25 8 L18 13 L25 18 Z M4 18.5 H24 L16.5 13.5 L14 15.5 L11.5 13.5 Z" fill-rule="evenodd"/>
      </svg>
      <span>dan@brenwick.example</span>
    </p>
  </div>
</body>
</html>
```